Flyer Jahreskonzert Gemischter Chor
Zielgruppe
Wir sind ein gemischter Chor aus der Schweiz unsere Mitglieder sind zwischen 20 und 70 Jahre jung und singen Querbeet durch die Musik von Lenz bis Velvix.
Das diesjährige Programm setzt sich aus Liedern von Gerd Palmow ( Schöne Grüße vom Hafen, Noch einmal ohne Zucker, nach 40 Wintern, Spanischer Mond, Klaus Wendlinger (Der bunte Garten), Gustav Rolf (Unter der Brücke), Walter Fischbeck(Tiefsee), und Miles Carver (Walk along the river slowly) zusammen.
Konzerttitel : 'Noch einmal ohne Zucker'
Daher würde ein 'süßes' Design passen, das ist aber nicht Bedingung, der Konzerttitel könnte auch noch angepasst werden.
Weitere Infos auf www.feierstimmen-beispiel.ch
Aufgabenstellung
Wir brauchen eine Vorderseite für einen Konzert Flyer Format A5 hochformat als Werbung für unser Jahreskonzert.
Text:
Konzert Feierstimmen Uerikon
Samstag 8. November 2014, 17:00Uhr
Uerikon/Stäfa
Singsaal Schulhaus Lindenhalde
Sonntag 9. November 2014, 17:00Uhr
Uetikon am See
Falkenhofsaal

```html
<!DOCTYPE html>
<html lang="de">
<head>
<meta charset="utf-8">
<title>Konzert Feierstimmen Uerikon</title>
<link rel="stylesheet" href="https://fonts.googleapis.com/css2?family=Kanit:ital,wght@1,800&family=Barlow:wght@500;700&display=swap">
<style>
  :root {
    --backdrop: #d9d9d9;
    --paper: #ffffff;
    --pink: #c2187e;
    --violet: #7a1c8c;
    --violet-dark: #6a1a7e;
    --ink: #1f1f1f;
    --cream-light: #f7f7f5;
    --cream-shade: #d6d6d2;
  }
  * { margin: 0; padding: 0; box-sizing: border-box; }
  html, body {
    width: 1162px; height: 1200px; overflow: hidden;
    background: var(--backdrop);
  }
  .flyer {
    position: absolute; left: 185px; top: 40px;
    width: 792px; height: 1120px;
    background: var(--paper);
    overflow: hidden;
    box-shadow: 0 4px 18px rgba(0,0,0,0.18);
  }
  .flyer__notes-art {
    position: absolute; left: 40px; top: 60px; width: 360px; height: 360px;
    border-radius: 50%;
    background: radial-gradient(circle, rgba(150,150,150,0.28) 0%, rgba(150,150,150,0.12) 45%, rgba(255,255,255,0) 70%);
  }
  .flyer__cream-photo {
    position: absolute; right: 0; bottom: 0; width: 470px; height: 560px;
    background:
      radial-gradient(ellipse at 60% 70%, var(--cream-light) 0%, #ebebe8 45%, rgba(255,255,255,0) 75%),
      linear-gradient(160deg, rgba(255,255,255,0) 0%, var(--cream-shade) 60%, #e4e4e1 100%);
    opacity: 0.9;
  }
  .title {
    position: absolute; left: 60px; top: 28px; width: 660px;
    text-align: right;
    font-family: "Kanit", sans-serif; font-style: italic; font-weight: 800;
    text-transform: uppercase; line-height: 0.82;
  }
  .title__big { display: block; font-size: 150px; color: var(--pink); letter-spacing: -2px; }
  .title__mid { display: block; font-size: 78px; color: var(--violet); margin: -8px 0 -4px; letter-spacing: -1px; }
  .tagline {
    position: absolute; left: 212px; top: 488px;
    background: var(--violet-dark); color: var(--paper);
    font-family: "Barlow", sans-serif; font-weight: 700; font-size: 34px;
    padding: 6px 20px; box-shadow: 3px 3px 6px rgba(0,0,0,0.25);
  }
  .event { position: absolute; left: 50px; font-family: "Barlow", sans-serif; }
  .event--sat { top: 590px; }
  .event--sun { top: 790px; }
  .event__day, .event__date {
    font-family: "Kanit", sans-serif; font-style: italic; font-weight: 800;
    text-transform: uppercase; color: var(--violet); line-height: 1.05;
  }
  .event__day { font-size: 58px; }
  .event__date { font-size: 44px; }
  .event__info { margin-top: 10px; font-size: 23px; font-weight: 500; color: var(--ink); line-height: 1.3; }
  .website {
    position: absolute; left: 50px; top: 1020px;
    font-family: "Barlow", sans-serif; font-weight: 700; font-size: 27px; color: var(--ink);
  }
</style>
</head>
<body>
  <main class="flyer">
    <div class="flyer__notes-art" role="img" aria-label="Faint swirl of music notes"></div>
    <div class="flyer__cream-photo" role="img" aria-label="Close-up photo of whipped cream"></div>

    <h1 class="title">
      <span class="title__big">Noch</span>
      <span class="title__mid">Einmal ohne</span>
      <span class="title__big">Zucker</span>
    </h1>

    <p class="tagline">Konzert Feierstimmen Uerikon</p>

    <section class="event event--sat">
      <p class="event__day">Samstag</p>
      <p class="event__date">8. November 2014</p>
      <p class="event__info">17.00 Uhr · Uerikon/Stäfa<br>Singsaal Schulhaus Lindenhalde</p>
    </section>

    <section class="event event--sun">
      <p class="event__day">Sonntag</p>
      <p class="event__date">9. November 2014</p>
      <p class="event__info">17.00 Uhr · Uetikon am See<br>Falkenhofsaal</p>
    </section>

    <p class="website">www.feierstimmen-beispiel.ch</p>
  </main>
</body>
</html>
```